Logo for a small law firm
phrase "Trial Lawyers" should appear
Professional
Colby, Fenwick & Lusk
R. Tomasz Colby
3817 SW 58th Avenue Suite 314 Miami, Florida 33155
tomasz@colbylegal.net
The name of the firm should appear at the top and the phrase "Trial Lawyers" below it
rtomaszcolby rtomaszcolby
Yes, of course. The name is Colby, Fenwick & Lusk. I am looking for a professional business logo/tradename for use on all stationery.
VelunoStudioWorks VelunoStudioWorks
Hi Sir/Madam, Can you please tell me the firm name which you want to put in the logo and which kind of logo you want? Thnx.

```html
<!DOCTYPE html>
<html lang="en">
<head>
<meta charset="utf-8">
<title>Colby, Fenwick &amp; Lusk — Trial Lawyers</title>
<link href="https://fonts.googleapis.com/css2?family=Lato:wght@400;700&display=swap" rel="stylesheet">
<style>
  :root {
    --navy: #2a2572;
    --ink: #1a1a1a;
    --paper: #ffffff;
    --muted: #3a3a3a;
  }
  * { margin: 0; padding: 0; box-sizing: border-box; }
  html, body { width: 1200px; height: 901px; overflow: hidden; background: var(--paper); }
  .canvas { position: relative; width: 1200px; height: 901px; background: var(--paper); font-family: "Lato", Arial, sans-serif; }

  .brand {
    position: absolute; transform: translateX(-50%);
    text-align: center; white-space: nowrap;
    font-family: "Lato", Arial, sans-serif; font-weight: 700;
    color: var(--navy); line-height: 1.15;
  }
  .brand .name { display: flex; align-items: center; justify-content: center; }
  .brand .mark { display: inline-block; background: currentColor; }

  .brand--main { left: 600px; top: 228px; }
  .brand--main .name { font-size: 46px; gap: 16px; }
  .brand--main .mark { width: 16px; height: 16px; }
  .brand--main .tagline { font-size: 21px; letter-spacing: 3.5px; margin-top: 10px; }

  .card { position: absolute; width: 576px; height: 320px; box-shadow: 2px 4px 8px rgba(0,0,0,0.35); }
  .card--front { left: 19px; top: 509px; background: var(--navy); }
  .card--back { left: 605px; top: 509px; background: var(--paper); }

  .brand--front { left: 288px; top: 136px; color: var(--paper); }
  .brand--front .name { font-size: 22px; gap: 8px; }
  .brand--front .mark { width: 8px; height: 8px; }
  .brand--front .tagline { font-size: 10px; letter-spacing: 1.8px; margin-top: 4px; }

  .website {
    position: absolute; left: 0; right: 0; top: 280px; text-align: center;
    font-size: 14px; color: var(--paper);
  }

  .brand--back { left: 283px; top: 46px; }
  .brand--back .name { font-size: 23px; gap: 8px; }
  .brand--back .mark { width: 8px; height: 8px; }
  .brand--back .tagline { font-size: 10px; letter-spacing: 1.8px; margin-top: 4px; }

  .accent-bar { position: absolute; left: 5px; top: 139px; width: 7px; height: 144px; background: var(--ink); }
  .contact { position: absolute; left: 43px; top: 143px; color: var(--muted); }
  .contact .address { font-size: 13px; line-height: 20px; }
  .contact .phone { font-size: 15px; font-weight: 700; color: var(--ink); margin-top: 12px; }
  .contact .email { font-size: 13px; margin-top: 18px; }

  .person { position: absolute; left: 348px; top: 198px; }
  .person .name { font-size: 21px; color: var(--navy); }
  .person .role { font-size: 12px; color: var(--muted); margin-top: 4px; }
</style>
</head>
<body>
<div class="canvas">

  <div class="brand brand--main">
    <div class="name"><span class="mark"></span>Colby, Fenwick &amp; Lusk</div>
    <div class="tagline">TRIAL LAWYERS</div>
  </div>

  <div class="card card--front">
    <div class="brand brand--front">
      <div class="name"><span class="mark"></span>Colby, Fenwick &amp; Lusk</div>
      <div class="tagline">TRIAL LAWYERS</div>
    </div>
    <div class="website">www.colbylegal.net</div>
  </div>

  <div class="card card--back">
    <div class="brand brand--back">
      <div class="name"><span class="mark"></span>Colby, Fenwick &amp; Lusk</div>
      <div class="tagline">TRIAL LAWYERS</div>
    </div>
    <div class="accent-bar"></div>
    <div class="contact">
      <div class="address">3817 SW 58th Avenue<br>Suite 314<br>Miami, Florida 33155</div>
      <div class="phone">(305) 728-4190</div>
      <div class="email">tomasz@colbylegal.net</div>
    </div>
    <div class="person">
      <div class="name">R. Tomasz Colby</div>
      <div class="role">Attorneys</div>
    </div>
  </div>

</div>
</body>
</html>
```